Stationary (letterhead, envelopes, business cards and e-mail signature) for law firm
Law Office of Warren T. Felding
Creative Brief
Professional
Warren T. Felding
Attorney at Law
41 Linden Court, Suite 500 Maple Falls, Arcadia 92731
wfelding@lawwtf-example.com
www.lawwtf-example.com
I would also like my direct dial phone number to appear on the card (in addition to my main number. The Direct number is (714) 555-0187
I would like my logo and maybe my website address to appear on the back. Please be creative.

```html
<!DOCTYPE html>
<html lang="en">
<head>
<meta charset="utf-8">
<title>Law Office of Warren T. Felding — Business Cards</title>
<link rel="stylesheet" href="https://fonts.googleapis.com/css2?family=Cinzel:wght@400;600&family=Lato:wght@400;700&display=swap">
<style>
  :root {
    --canvas: #e9e7e3;
    --card: #ffffff;
    --navy: #27305a;
    --navy-ink: #2c3560;
    --muted: #6d7183;
    --on-navy: #e8eaf2;
    --rule: #c9ccd8;
  }
  * { box-sizing: border-box; margin: 0; padding: 0; }
  html, body { width: 1200px; height: 629px; overflow: hidden; }
  body {
    background: var(--canvas);
    font-family: "Lato", sans-serif;
    display: flex;
    align-items: center;
    justify-content: center;
    gap: 40px;
  }
  .card {
    width: 540px;
    height: 310px;
    background: var(--card);
    box-shadow: 0 6px 18px rgba(0,0,0,0.12);
    position: relative;
    overflow: hidden;
  }
  .brand {
    display: flex;
    align-items: center;
    gap: 14px;
    color: var(--navy-ink);
    font-family: "Cinzel", serif;
    font-weight: 400;
  }
  .brand-mark {
    width: 34px;
    height: 34px;
    background: var(--navy);
    flex: none;
  }
  .brand-name { line-height: 1.25; letter-spacing: 0.08em; white-space: nowrap; }
  .brand-name .line-small { font-size: 12px; display: block; }
  .brand-name .line-large { font-size: 20px; display: block; }

  /* front */
  .card-front {
    display: flex;
    flex-direction: column;
    justify-content: center;
    align-items: center;
    gap: 30px;
  }
  .card-front .brand { transform: translateX(-10px); }
  .website {
    font-size: 11px;
    letter-spacing: 0.35em;
    color: var(--muted);
    text-transform: uppercase;
  }

  /* back */
  .card-back .top {
    height: 150px;
    display: flex;
    align-items: center;
    padding-left: 40px;
  }
  .card-back .top .brand-name .line-small { font-size: 11px; }
  .card-back .top .brand-name .line-large { font-size: 18px; }
  .card-back .band {
    position: absolute;
    left: 0; right: 0; bottom: 0;
    height: 160px;
    background: var(--navy);
    color: var(--on-navy);
    display: flex;
    padding: 28px 30px 0 40px;
    justify-content: space-between;
  }
  .card-back .band::before {
    content: "";
    position: absolute;
    left: 0; right: 0; top: 0;
    height: 3px;
    background: var(--rule);
    opacity: 0.5;
  }
  .person .name {
    font-family: "Cinzel", serif;
    font-size: 15px;
    letter-spacing: 0.06em;
    white-space: nowrap;
  }
  .person .title {
    font-size: 9px;
    letter-spacing: 0.3em;
    text-transform: uppercase;
    margin-top: 5px;
    opacity: 0.85;
  }
  .person .email {
    font-size: 10px;
    letter-spacing: 0.05em;
    margin-top: 40px;
    white-space: nowrap;
  }
  .contact-list { list-style: none; display: flex; flex-direction: column; gap: 8px; width: 228px; }
  .contact-list li {
    display: flex;
    align-items: flex-start;
    gap: 10px;
    font-size: 10px;
    line-height: 1.35;
    letter-spacing: 0.04em;
    white-space: nowrap;
  }
  .contact-list svg {
    width: 14px; height: 14px; flex: none;
    fill: var(--on-navy);
  }
</style>
</head>
<body>

  <section class="card card-front" aria-label="Business card front">
    <div class="brand">
      <span class="brand-mark"></span>
      <span class="brand-name">
        <span class="line-small">Law Office of</span>
        <span class="line-large">Warren T. Felding</span>
      </span>
    </div>
    <p class="website">www.lawwtf-example.com</p>
  </section>

  <section class="card card-back" aria-label="Business card back">
    <div class="top">
      <div class="brand">
        <span class="brand-mark"></span>
        <span class="brand-name">
          <span class="line-small">Law Office of</span>
          <span class="line-large">Warren T. Felding</span>
        </span>
      </div>
    </div>
    <div class="band">
      <div class="person">
        <p class="name">Warren T. Felding</p>
        <p class="title">Attorney at Law</p>
        <p class="email">wfelding@lawwtf-example.com</p>
      </div>
      <ul class="contact-list">
        <li>
          <svg viewBox="0 0 24 24" aria-hidden="true"><path d="M12 2a7 7 0 0 0-7 7c0 5 7 13 7 13s7-8 7-13a7 7 0 0 0-7-7zm0 9.5A2.5 2.5 0 1 1 12 6.5a2.5 2.5 0 0 1 0 5z"/></svg>
          <span>41 Linden Court, Suite 500<br>Maple Falls, Arcadia 92731</span>
        </li>
        <li>
          <svg viewBox="0 0 24 24" aria-hidden="true"><path d="M6.6 10.8a15 15 0 0 0 6.6 6.6l2.2-2.2a1 1 0 0 1 1-.25 11.4 11.4 0 0 0 3.6.57 1 1 0 0 1 1 1V20a1 1 0 0 1-1 1A17 17 0 0 1 3 4a1 1 0 0 1 1-1h3.5a1 1 0 0 1 1 1c0 1.25.2 2.45.57 3.57a1 1 0 0 1-.25 1z"/></svg>
          <span>(555) 555-0142</span>
        </li>
        <li>
          <svg viewBox="0 0 24 24" aria-hidden="true"><path d="M6.6 10.8a15 15 0 0 0 6.6 6.6l2.2-2.2a1 1 0 0 1 1-.25 11.4 11.4 0 0 0 3.6.57 1 1 0 0 1 1 1V20a1 1 0 0 1-1 1A17 17 0 0 1 3 4a1 1 0 0 1 1-1h3.5a1 1 0 0 1 1 1c0 1.25.2 2.45.57 3.57a1 1 0 0 1-.25 1z"/></svg>
          <span>(555) 555-0187</span>
        </li>
        <li>
          <svg viewBox="0 0 24 24" aria-hidden="true"><path d="M12 2a10 10 0 1 0 0 20 10 10 0 0 0 0-20zm0 2c.9 0 2.2 2 2.7 5H9.3C9.8 6 11.1 4 12 4zM4.3 11h3a17 17 0 0 0 0 2h-3a8 8 0 0 1 0-2zm5 0h5.4a15 15 0 0 1 0 2H9.3a15 15 0 0 1 0-2zm7.4 0h3a8 8 0 0 1 0 2h-3a17 17 0 0 0 0-2zM9.3 15h5.4c-.5 3-1.8 5-2.7 5s-2.2-2-2.7-5z"/></svg>
          <span>www.lawwtf-example.com</span>
        </li>
      </ul>
    </div>
  </section>

</body>
</html>
```